Eastvale Physiotherapy Website www.eastvalephysiotherapy.com.au

Create Wordpress website for Eastvale Physiotherapy which aligns with our other locations www.marrowbankphysiotherapy,com.au. We would like the website to present in a similar fashion to our exisiting site with similar headings and layout. We will then alter the text to make it location specific.

Coding

Coded - Design and coding required

Number of Pages Required

1 page

Font styles to use
Sans Serif

Requirements
Must have
• Colours of the website must match the colours of the colour Eastvale Physiotherapy logo
• Website must be complimentary to existing websites,
• www.marrowbankphysiotherapy.com.au
• www.marrowbankpilatesandrehab.com.au

```html
<!DOCTYPE html>
<html lang="en">
<head>
<meta charset="utf-8">
<title>Eastvale Physiotherapy</title>
<link rel="stylesheet" href="https://fonts.googleapis.com/css2?family=Open+Sans:wght@400;600&family=Roboto+Condensed:wght@400&display=swap">
<style>
:root{
  --green:#7dbfa5;
  --green-dark:#5fa88c;
  --navy:#23325f;
  --blue:#2f7db6;
  --blue-deep:#1f6aa3;
  --ink:#1c1c1c;
  --text:#5a5a5a;
  --muted:#8a8a8a;
  --grey-bg:#efefef;
  --line:#d8d8d8;
  --white:#ffffff;
}
*{box-sizing:border-box;margin:0;padding:0}
html,body{width:1200px;height:3051px;overflow:hidden;background:var(--white)}
body{position:relative;font-family:"Open Sans",sans-serif;color:var(--text)}
.abs{position:absolute}
h1,h2,h3{font-family:"Roboto Condensed",sans-serif;font-weight:400;color:var(--ink)}

/* header */
.site-header{left:0;top:0;width:1200px;height:136px}
.brand{left:92px;top:44px;display:flex;align-items:center;gap:12px;font-family:"Open Sans",sans-serif;font-weight:600;font-size:22px;color:var(--navy)}
.brand-dot{width:26px;height:26px;border-radius:50%;background:var(--navy)}
.main-nav{right:90px;top:52px;display:flex;gap:38px;font-size:17px;color:var(--ink)}
.main-nav .active{color:var(--green)}

/* hero */
.hero{left:0;top:136px;width:1200px;height:534px;background:linear-gradient(90deg,#e9ecee 0%,#f6f7f7 45%,#ffffff 75%,#eef1f2 100%)}
.hero-title{right:92px;top:92px;text-align:right;line-height:1.05}
.hero-title .line-1{display:block;font-family:"Roboto Condensed",sans-serif;font-size:64px;color:var(--green)}
.hero-title .line-2{display:block;font-family:"Roboto Condensed",sans-serif;font-size:50px;color:var(--ink)}
.slider-dots{left:90px;top:480px;display:flex;gap:6px}
.slider-dots span{width:24px;height:24px;border-radius:50%;background:#8d8d8d;opacity:.8}

/* welcome */
.welcome{left:0;top:700px;width:1200px;text-align:center}
.welcome h1{font-size:34px;margin-top:36px}
.welcome p.intro{width:944px;margin:22px auto 0;font-size:14.6px;line-height:25px;text-align:justify;text-align-last:center}
.btn{display:inline-block;background:var(--green);color:var(--white);border-radius:24px;font-size:15px;text-transform:uppercase}
.btn-book{margin-top:30px;width:214px;height:46px;line-height:46px}
.welcome .note{margin-top:34px;font-size:23px;line-height:40px;color:var(--ink)}

/* services */
.services{left:0;top:1185px;width:1200px;height:481px;background:linear-gradient(180deg,var(--blue) 0%,#3a88bf 60%,#4e8fb0 100%)}
.services h2{position:absolute;left:0;top:62px;width:1200px;text-align:center;color:var(--white);font-size:34px}
.service{position:absolute;top:162px;width:230px;text-align:center;color:var(--white)}
.service .icon{width:114px;height:114px;border-radius:50%;background:var(--white);margin:0 auto;display:flex;align-items:center;justify-content:center}
.service h3{color:var(--white);font-family:"Open Sans",sans-serif;font-size:19px;margin-top:22px}
.service p{font-size:13.5px;line-height:20px;margin-top:8px}
.service .more{font-size:13px;margin-top:10px}
.arrow{top:270px}

/* about */
.about-photo{left:112px;top:1775px;width:300px;height:300px;border-radius:50%;border:2px solid #777;padding:6px}
.about-photo div{width:100%;height:100%;border-radius:50%;background:radial-gradient(circle at 50% 40%,#e8dcd6 0%,#cfc3c2 55%,#b9b2b6 100%)}
.about{left:437px;top:1795px;width:660px}
.about h2{font-size:33px}
.about p{margin-top:16px;font-size:14.2px;line-height:26px;text-align:justify}
.btn-read{margin-top:18px;width:98px;height:36px;line-height:36px;font-size:11px;text-align:center}

/* blog */
.blog{left:0;top:2135px;width:1200px;height:600px;background:var(--grey-bg)}
.blog h2{position:absolute;top:62px;width:1200px;text-align:center;font-size:33px}
.post{position:absolute;top:150px;width:315px;height:365px;background:var(--white);box-shadow:0 4px 14px rgba(0,0,0,.18);padding:13px;text-align:center}
.post .thumb{height:190px}
.post h3{font-family:"Open Sans",sans-serif;font-size:17px;margin-top:28px}
.post p{font-size:13.5px;line-height:22px;color:var(--muted);margin-top:10px}
.post .more{font-size:13px;color:var(--blue-deep);margin-top:10px}

/* footer */
.footer-brand{left:100px;top:2874px;display:flex;align-items:center;gap:10px;font-weight:600;font-size:19px;color:var(--navy)}
.footer-col h4{font-weight:400;font-size:16px;color:var(--ink);letter-spacing:.5px}
.contact{left:392px;top:2808px;font-size:12.8px;line-height:21px;color:#444}
.contact ul{list-style:none;margin-top:26px}
.newsletter{left:778px;top:2808px;font-size:12.8px;color:#444}
.newsletter p{margin-top:26px}
.signup{display:flex;margin-top:18px}
.signup .field{width:245px;height:31px;border:1px solid #cfcfcf;font-size:12px;line-height:29px;padding-left:8px;color:var(--muted)}
.signup .submit{width:64px;height:31px;background:var(--green);color:var(--white);font-size:12px;line-height:31px;text-align:center}
.rule{left:90px;top:2983px;width:1022px;height:1px;background:var(--line)}
.copyright{left:90px;top:3008px;font-size:12.5px;color:#333}
.social{left:986px;top:3004px;display:flex;gap:10px}
.social span{width:22px;height:22px;border-radius:3px;background:#5a5a5a}
</style>
</head>
<body>

<header class="abs site-header">
  <div class="abs brand"><span class="brand-dot"></span>Eastvale Physiotherapy</div>
  <nav class="abs main-nav">
    <span class="active">Home</span><span>About</span><span>Service</span><span>Conditions</span><span>Health tips</span><span>Blog</span><span>Contact</span>
  </nav>
</header>

<section class="abs hero" role="img" aria-label="Woman in a white top doing a bridge exercise on a mat in a bright studio">
  <div class="abs hero-title"><span class="line-1">Eastvale</span><span class="line-2">Physiotherapy</span></div>
  <div class="abs slider-dots"><span></span><span></span></div>
</section>

<section class="abs welcome">
  <h1>WELCOME TO EASTVALE PHYSIOTHERAPY</h1>
  <p class="intro">Eastvale Physiotherapy is an innovative physiotherapy practice offering comprehensive services by experienced and highly-qualified physiotherapists. We achieve outstanding clinical results for a broad range of common conditions including: back pain, neck pain, headache, migraine, shoulder pain, sports injuries, vertigo, knee pain, incontinence, persistent pelvic pain and women's health and men's health issues. We are confident our practice will offer a service that stands apart, as we value excellence in quality care delivered by highly-educated and experienced physiotherapists.</p>
  <span class="btn btn-book">Book online here</span>
  <p class="note">*Please note not all practitioners are available online –<br>please call 95550142&nbsp; to speak with our reception team.</p>
</section>

<section class="abs services" role="img" aria-label="Blue-tinted background of people stretching outdoors">
  <h2>OUR SERVICES</h2>
  <svg class="abs arrow" style="left:60px" width="18" height="30" viewBox="0 0 18 30"><path d="M15 2 3 15l12 13" fill="none" stroke="#fff" stroke-width="2.5"/></svg>
  <svg class="abs arrow" style="left:1134px" width="18" height="30" viewBox="0 0 18 30"><path d="M3 2l12 13L3 28" fill="none" stroke="#fff" stroke-width="2.5"/></svg>

  <div class="service" style="left:85px">
    <div class="icon"><svg width="44" height="44" viewBox="0 0 44 44"><path d="M22 6v32M6 22h32" stroke="#2f8fe0" stroke-width="7" stroke-linecap="round"/></svg></div>
    <h3>Physiotherapy</h3>
    <p>Our team of experienced physio-<br>therapists have a wide range</p>
    <div class="more">Learn More -&gt;</div>
  </div>
  <div class="service" style="left:355px">
    <div class="icon"><svg width="44" height="44" viewBox="0 0 44 44"><circle cx="22" cy="22" r="15" fill="none" stroke="#2f8fe0" stroke-width="5"/><circle cx="22" cy="22" r="5" fill="#2f8fe0"/></svg></div>
    <h3>Knee Clinic</h3>
    <p>The knee pain clinic provides a<br>complete approach for those</p>
    <div class="more">Learn More -&gt;</div>
  </div>
  <div class="service" style="left:627px">
    <div class="icon"><svg width="54" height="46" viewBox="0 0 54 46"><rect x="3" y="4" width="40" height="28" rx="2" fill="none" stroke="#2f8fe0" stroke-width="3"/><path d="M17 40h12M23 32v8M43 22h5v14" fill="none" stroke="#2f8fe0" stroke-width="3"/><path d="M9 22l6-8 6 10 6-6 6 4" fill="none" stroke="#2f8fe0" stroke-width="2"/></svg></div>
    <h3>Real Time Ultrasound</h3>
    <p>Physiotherapists use real-time<br>ultrasound to examine how the</p>
    <div class="more">Learn More -&gt;</div>
  </div>
  <div class="service" style="left:885px">
    <div class="icon"><svg width="24" height="56" viewBox="0 0 24 56"><rect x="3" y="2" width="18" height="8" rx="3" fill="#2f8fe0"/><rect x="3" y="13" width="18" height="8" rx="3" fill="#2f8fe0"/><rect x="3" y="24" width="18" height="8" rx="3" fill="#2f8fe0"/><rect x="3" y="35" width="18" height="8" rx="3" fill="#2f8fe0"/><rect x="3" y="46" width="18" height="8" rx="3" fill="#2f8fe0"/></svg></div>
    <h3>Chronic Pain</h3>
    <p>We all understand the complex<br>nature of chronic pain and</p>
    <div class="more">Learn More -&gt;</div>
  </div>
</section>

<div class="abs about-photo"><div role="img" aria-label="Older woman with a towel after exercise at the gym"></div></div>
<section class="abs about">
  <h2>ABOUT US</h2>
  <p>Marrowbank Pilates &amp; Rehab is dedicated to clinical excellence and innovation, offering comprehensive fitness and rehabilitation programs from its beautifully inspiring Melbourne fringe studio in Marrowbank. Known for their friendly and personable approach, our Pilates Instructors conduct classes in small groups to promote a greater learning and interaction. Experienced physiotherapists are also available to provide 1:1 consultations for clients.</p>
  <span class="btn btn-read">Read more »</span>
</section>

<section class="abs blog">
  <h2>LATEST BLOG</h2>
  <article class="post" style="left:88px">
    <div class="thumb" role="img" aria-label="Tired man at a desk holding his head" style="background:linear-gradient(135deg,#d9dde2,#a9b3bf 60%,#7d8793)"></div>
    <h3>The 2017 MBP/MBPR Cook-Off</h3>
    <p>The point of using Lorem Ipsum is that<br>it has a more-or-less normal</p>
    <div class="more">Read More »</div>
  </article>
  <article class="post" style="left:443px">
    <div class="thumb" role="img" aria-label="Runner's legs on a grassy hilltop at sunset" style="background:linear-gradient(180deg,#9a7a55,#c89a5e 45%,#6b5a3c)"></div>
    <h3>Volunteers for shoulder</h3>
    <p>The point of using Lorem Ipsum is that<br>it has a more-or-less normal</p>
    <div class="more">Read More »</div>
  </article>
  <article class="post" style="left:799px">
    <div class="thumb" role="img" aria-label="Women doing Pilates on reformer machines in a studio" style="background:linear-gradient(135deg,#e7e7ea,#c3c6cc 55%,#9ca3ad)"></div>
    <h3>it's more than just kegels!</h3>
    <p>The point of using Lorem Ipsum is that<br>it has a more-or-less normal</p>
    <div class="more">Read More »</div>
  </article>
</section>

<footer>
  <div class="abs footer-brand"><span class="brand-dot" style="width:20px;height:20px"></span>Eastvale Physiotherapy</div>
  <div class="abs footer-col contact">
    <h4>CONTACT US</h4>
    <ul>
      <li>Address : 41-43 Harbour Lane</li>
      <li>Marrowbank VIC 3999</li>
      <li>Phone :&nbsp; 03 9555 0142</li>
      <li>Email : admin@marrowbankpilatesandrehab.com.au</li>
    </ul>
  </div>
  <div class="abs footer-col newsletter">
    <h4>LET'S STAY IN TOUCH!</h4>
    <p>Your about us information would fit here nicely.</p>
    <div class="signup"><span class="field">Email address</span><span class="submit">Submit</span></div>
  </div>
  <div class="abs rule"></div>
  <div class="abs copyright">Copyright © 2018. All Rights Reserved</div>
  <div class="abs social"><span></span><span></span><span></span><span></span></div>
</footer>

</body>
</html>
```